Financial Advisor needs a BOLD Business Card

I need a business card that is professional, and is also eye-catching and memorable. I would like to include my photo (several different professional photos have been uploaded). Preferred primary color is blue, or green, or dark purple. The final design should have a modern/contemporary look while communicating a professional image.

Target Market(s)

Individual Investors and Small Business Owners

Industry/Entity Type

Business

Contact Information for Business Card

[side 1:] Dale Korvanek Financial Advisor 58271 Marbleton Creek Rd., #340 St. Louis, MO 63907 (314) 555-0182 main (314) 555-0927 cell (314) 555-0346 fax daleK@qrvlx.com [side 2:] Life Insurance | Retirement | Employee Benefits

Font styles to use
Serif
Sans Serif

Requirements
Must have
• [disclaimer, text can be 7-9 point:] Securities offered through the B.W. Harbor Trading Company. Member NARCU/TLOB. Four Quarry Plaza, Cincinnati, Ohio 45917. 513-555-0263. Investment Advisory Services offered through B.W. Holdings Management Company.
Nice to have
• Bright, Light & Airy feel on Side 1 with contact data, bold patterns, high color contrast, modern or 3D look
Should not have
• Any symbols referring to money (e.g. $)

```html
<!DOCTYPE html>
<html lang="en">
<head>
<meta charset="utf-8">
<title>Dale Korvanek – Financial Advisor Business Card</title>
<link rel="stylesheet" href="https://fonts.googleapis.com/css2?family=Varela+Round&family=Marcellus+SC&family=Arimo:wght@400;700&display=swap">
<style>
  :root {
    --stage: #c9cacc;
    --blue: #0f78bf;
    --blue-light: #2a95d6;
    --blue-deep: #0a64a8;
    --name-blue: #1a7fc4;
    --ink-grey: #4a4d52;
    --silver-light: #eef0f2;
    --silver-dark: #9ea3a8;
    --white: #ffffff;
    --card-radius: 24px;
  }
  * { box-sizing: border-box; margin: 0; padding: 0; }
  html, body { width: 1200px; height: 900px; overflow: hidden; }
  body {
    background: var(--stage);
    position: relative;
    font-family: "Arimo", Arial, sans-serif;
  }
  .card {
    position: absolute;
    top: 300px;
    width: 530px;
    height: 303px;
    border-radius: var(--card-radius);
    overflow: hidden;
    box-shadow: 0 10px 24px rgba(0,0,0,0.22);
  }
  .card--back { left: 45px; }
  .card--front { left: 625px; }

  /* Back side */
  .card--back {
    background: radial-gradient(ellipse at 40% 40%, var(--blue-light) 0%, var(--blue) 55%, var(--blue-deep) 100%);
  }
  .services {
    position: absolute;
    top: 128px;
    left: 0;
    width: 100%;
    text-align: center;
    font-family: "Marcellus SC", Georgia, serif;
    font-size: 15px;
    letter-spacing: 2.4px;
    color: #e4f1fb;
  }
  .services .sep { margin: 0 10px; opacity: 0.8; }

  .disclaimer {
    position: absolute;
    left: 28px;
    right: 28px;
    bottom: 12px;
    font-size: 7.5px;
    line-height: 10px;
    text-align: center;
    color: #cfe3f3;
  }

  .brand {
    position: absolute;
    display: flex;
    align-items: center;
  }
  .brand__mark {
    background: linear-gradient(135deg, var(--silver-light), var(--silver-dark));
    border-radius: 4px;
  }
  .brand__rule { width: 1px; background: currentColor; opacity: 0.6; }
  .brand__name {
    font-family: "Varela Round", Arial, sans-serif;
    line-height: 1;
  }
  .brand__title {
    font-family: "Marcellus SC", Georgia, serif;
    line-height: 1;
  }

  .card--back .brand { right: 34px; bottom: 52px; color: #dbe9f5; }
  .card--back .brand__mark { width: 36px; height: 36px; margin-right: 9px; }
  .card--back .brand__rule { height: 38px; margin-right: 8px; }
  .card--back .brand__name { font-size: 20px; color: #dbe9f5; }
  .card--back .brand__title { font-size: 9.5px; letter-spacing: 2.6px; color: #dbe9f5; margin-top: 4px; }

  /* Front side */
  .card--front { background: var(--white); }
  .front__top {
    position: absolute;
    inset: 0 0 auto 0;
    height: 160px;
    background: var(--white);
  }
  .card--front .brand { left: 34px; top: 44px; color: var(--ink-grey); }
  .card--front .brand__mark { width: 68px; height: 68px; margin-right: 14px; }
  .card--front .brand__rule { height: 66px; margin-right: 12px; }
  .card--front .brand__name { font-size: 31px; color: var(--name-blue); }
  .card--front .brand__title { font-size: 14px; letter-spacing: 3.4px; color: var(--ink-grey); margin-top: 8px; }

  .portrait {
    position: absolute;
    right: 26px;
    top: 14px;
    width: 118px;
    height: 138px;
    background: linear-gradient(180deg, #dfe3ea 0%, #5d6470 45%, #2a2e36 100%);
  }
  .silver-band {
    position: absolute;
    left: 0; right: 0;
    top: 152px;
    height: 12px;
    background: linear-gradient(180deg, var(--silver-light), var(--silver-dark));
  }
  .front__bottom {
    position: absolute;
    left: 0; right: 0; bottom: 0;
    top: 164px;
    background: radial-gradient(ellipse at 50% 30%, var(--blue-light) 0%, var(--blue) 60%, var(--blue-deep) 100%);
  }
  .contact {
    position: absolute;
    left: 34px;
    top: 14px;
    list-style: none;
    color: var(--white);
    font-size: 14.5px;
    line-height: 19px;
  }
  .contact li { display: flex; align-items: flex-start; }
  .contact svg { width: 14px; height: 14px; margin: 2px 5px 0 0; flex: none; fill: #d7e6f3; }
  .contact .indent { padding-left: 19px; }
</style>
</head>
<body>

  <section class="card card--back" aria-label="Business card back">
    <p class="services">Life Insurance<span class="sep">|</span>Retirement<span class="sep">|</span>Employee Benefits</p>
    <div class="brand">
      <span class="brand__mark"></span>
      <span class="brand__rule"></span>
      <div>
        <div class="brand__name">Dale Korvanek</div>
        <div class="brand__title">Financial Advisor</div>
      </div>
    </div>
    <p class="disclaimer">Securities offered through the B.W. Harbor Trading Company. Member NARCU/TLOB. Four Quarry Plaza, Cincinnati, Ohio 45917. 513-555-0263. Investment Advisory Services offered through B.W. Holdings Management Company.</p>
  </section>

  <section class="card card--front" aria-label="Business card front">
    <div class="front__top">
      <div class="brand">
        <span class="brand__mark"></span>
        <span class="brand__rule"></span>
        <div>
          <div class="brand__name">Dale Korvanek</div>
          <div class="brand__title">Financial Advisor</div>
        </div>
      </div>
      <div class="portrait" role="img" aria-label="Portrait photo of the advisor in a dark suit and blue tie"></div>
    </div>
    <div class="silver-band"></div>
    <div class="front__bottom">
      <ul class="contact">
        <li><svg viewBox="0 0 14 14"><rect x="3" y="0.5" width="8" height="13" rx="1.5"/><rect x="4.5" y="2" width="5" height="8" fill="#0f78bf"/></svg>(314) 555-0927</li>
        <li><svg viewBox="0 0 14 14"><path d="M3 1l2.5 0 1 3-1.6 1.2c.8 1.7 2 2.9 3.7 3.7L9.8 7.3l3 1v2.6c0 .7-.6 1.2-1.3 1.1C6 11.4 2.4 7.8 2 2.3 1.9 1.6 2.4 1 3 1z"/></svg>(314) 555-0182</li>
        <li><svg viewBox="0 0 14 14"><rect x="4" y="1" width="6" height="4"/><rect x="1" y="5" width="12" height="6" rx="1"/><rect x="4" y="9" width="6" height="4" fill="#0f78bf" stroke="#d7e6f3"/></svg>(314) 555-0346</li>
        <li><svg viewBox="0 0 14 14"><rect x="1" y="3" width="12" height="9" rx="1"/><path d="M1.5 3.5L7 8l5.5-4.5" fill="none" stroke="#0f78bf" stroke-width="1.2"/></svg>daleK@qrvlx.com</li>
        <li><svg viewBox="0 0 14 14"><path d="M7 1L1 6.5h2V13h3V9h2v4h3V6.5h2z"/></svg>58271 Marbleton Creek Rd.,</li>
        <li class="indent">#340 St. Louis, MO 63907</li>
      </ul>
    </div>
  </section>

</body>
</html>
```